We need a flyer for our company. We test drugs, laser, LED or other light sources for phototoxicity on healthy volunteers.
You can use our website for an idea or imagine www.lumivanta.co.uk
Lumivanta has a well-established reputation in the field of drug- and chemical-induced phototoxicity and expertise in clinical studies of photoprotective agents, such as nutraceuticals and antioxidants and light-based device development and application. The team at Lumivanta has an international reputation in the field of UV and visible light measurement and our team has a truly multidisciplinary nature, with professionals including physicians, medical physicists, biochemists, technicians and nurses.

Target Market(s)

any pharmaceutical or cosmetical company

Industry/Entity Type

Cosmetic

Font styles to use
Serif

Colors

Designer to choose colors to be used in the design.

Requirements
Must have
• Clinical studies:
• Phototoxicity
• Photoallergy to topical agents
• Photoprotection by oral or topical agents
• Light-based devices
• Laboratory studies:
• Photosafety and photoxicity
• Photophysics and light source evaluation
Nice to have
• Can you reduce the amount of text and concentrate on this point?
• First page:
• • Lumivanta has a well-established reputation in the field of drug- and chemical-induced phototoxicity and expertise in clinical studies of photoprotective agents:
• such as nutraceuticals
• and antioxidants
• and light-based device development and application.
• • The team at Lumivanta has an international reputation in the field of UV and visible light measurement and our team has a truly multidisciplinary nature, with professionals including physicians, medical physicists, biochemists, technicians and nurses
• Second page:
• Clinical studies
• Phototoxicity
• Light-based devices
• Laboratory studies

```html
<!DOCTYPE html>
<html lang="en">
<head>
<meta charset="utf-8">
<title>Lumivanta flyer</title>
<link rel="stylesheet" href="https://fonts.googleapis.com/css2?family=Rokkitt:wght@400&display=swap">
<style>
  :root {
    --frame: #ffffff;
    --mist-light: #d6d6d6;
    --mist-mid: #b9b9b9;
    --panel-border: #f7f7f7;
    --body-ink: #465064;
    --brand-ink: #ffffff;
    --photo-tone-a: #dfe3e6;
    --photo-tone-b: #9fb3bf;
  }
  * { margin: 0; padding: 0; box-sizing: border-box; }
  html, body { width: 855px; height: 1200px; overflow: hidden; background: var(--frame); }
  .flyer {
    position: relative; width: 855px; height: 1200px; background: var(--frame);
    font-family: "Rokkitt", "Georgia", serif;
  }
  .backdrop {
    position: absolute; left: 18px; top: 16px; width: 820px; height: 1166px;
    background:
      radial-gradient(ellipse 60px 140px at 0% 45%, rgba(40,40,40,.75), transparent 70%),
      radial-gradient(ellipse 60px 160px at 100% 52%, rgba(40,40,40,.7), transparent 70%),
      radial-gradient(ellipse 160px 120px at 20% 12%, rgba(235,235,235,.9), transparent 70%),
      radial-gradient(ellipse 300px 90px at 50% 100%, rgba(60,60,60,.55), transparent 70%),
      radial-gradient(ellipse 90px 60px at 75% 25%, rgba(150,160,160,.6), transparent 70%),
      linear-gradient(180deg, var(--mist-mid) 0%, var(--mist-light) 25%, #c4c4c4 60%, #a9a9a9 100%);
  }
  .brand {
    position: absolute; left: 124px; top: 192px;
    font-size: 60px; line-height: 1; color: var(--brand-ink); font-weight: 400;
    letter-spacing: 1px;
  }
  .panel {
    position: absolute; left: 82px; top: 308px; width: 696px; height: 748px;
    background: var(--panel-border); border-radius: 5px;
    box-shadow: 0 26px 30px rgba(30,30,30,.45);
  }
  .panel-inner {
    position: absolute; left: 16px; top: 17px; width: 664px; height: 715px;
    background: linear-gradient(180deg, #c9c9c9 0%, #d8d8d8 30%, #c2c2c2 60%, #9c9c9c 100%);
  }
  .column {
    position: absolute; top: 20px; font-size: 20px; line-height: 28px;
    letter-spacing: -0.3px; color: var(--body-ink);
  }
  .column span { display: block; white-space: nowrap; }
  .column-left { left: 15px; }
  .column-right { left: 316px; }
  .clinic-photo {
    position: absolute; left: 0; top: 331px; width: 574px; height: 384px;
    background:
      linear-gradient(90deg, var(--photo-tone-b) 0%, var(--photo-tone-b) 18%, var(--photo-tone-a) 30%, #eef0f1 60%, #cfd5d8 100%);
    box-shadow: 8px 4px 14px rgba(40,40,40,.35);
  }
</style>
</head>
<body>
<div class="flyer">
  <div class="backdrop"></div>
  <div class="brand">Lumivanta</div>
  <section class="panel">
    <div class="panel-inner">
      <p class="column column-left">
        <span>• Lumivanta has a well-established</span>
        <span>reputation in the field of drug- and</span>
        <span>chemical-induced phototoxicity and</span>
        <span>expertise in clinical studies of</span>
        <span>photoprotective agents:</span>
        <span>- such as nutraceuticals</span>
        <span>- and antioxidants</span>
        <span>- and light-based device</span>
        <span>development and application.</span>
      </p>
      <p class="column column-right">
        <span>• The team at Lumivanta has an</span>
        <span>international reputation in the field of UV</span>
        <span>and visible light measurement and our</span>
        <span>team has a truly multidisciplinary</span>
        <span>nature, with professionals including</span>
        <span>physicians, medical physicists,</span>
        <span>biochemists, technicians and nurses</span>
      </p>
      <div class="clinic-photo" role="img" aria-label="Photograph of a clinical phototesting room with a treatment chair, lamp and equipment trolley"></div>
    </div>
  </section>
</div>
</body>
</html>
```